Inviting A6 Flyer for Church membership

We need an A6 size flyer for the church. We are looking for something fresh, inviting and impactful. Church new logo and current flyer design attached.
Back text as follows:
We would love to have you join us as our SPECIAL GUEST this Sunday at 10am.
You can find us at Harvest Gateway Family Church, 17-19 Meadowbrook Lane
(Behind Farley), Pellham Brook Village,KL7 2RT
For more information or for a chat, please call us on 07614 290457 / 07781 504316 or email church@hgfcuk.org
Target Market(s)
Church
Industry/Entity Type
Church
Colors
Designer to choose colors to be used in the design.
Requirements
Must have
- fresh, inviting and impactful.
- Chruch logo (attached)
Should not have
- Too much going on

```html
<!DOCTYPE html>
<html lang="en">
<head>
<meta charset="utf-8">
<title>Be Our Guest – A6 Flyer</title>
<link href="https://fonts.googleapis.com/css2?family=Oswald:wght@600&family=Roboto:wght@700&display=swap" rel="stylesheet">
<style>
  :root {
    --backdrop: #e9eaec;
    --slate: #2e3a46;
    --slate-soft: #37444f;
    --sky: #35a1dc;
    --sky-pale: #e3f2fb;
    --royal: #1f72c2;
    --ink: #2b3038;
    --white: #ffffff;
  }
  * { box-sizing: border-box; margin: 0; padding: 0; }
  html, body { width: 1200px; height: 775px; overflow: hidden; }
  body {
    background: var(--backdrop);
    font-family: "Roboto", Arial, sans-serif;
    position: relative;
  }
  .flyer {
    position: absolute;
    top: 68px;
    width: 454px;
    height: 640px;
    background: radial-gradient(circle at 30% 70%, var(--slate-soft), var(--slate) 70%);
    overflow: hidden;
    box-shadow: 0 6px 18px rgba(0,0,0,0.18);
  }
  .flyer--front { left: 90px; }
  .flyer--back { left: 656px; }

  .rule {
    position: absolute;
    top: 0;
    width: 6px;
    background: var(--sky);
  }

  /* Front */
  .flyer--front .rule { height: 100%; }
  .flyer--front .rule--left { left: 70px; }
  .flyer--front .rule--right { left: 378px; }
  .front-panel {
    position: absolute;
    left: 92px; top: 0;
    width: 270px; height: 460px;
    background: var(--sky);
    display: flex;
    align-items: center;
    justify-content: center;
  }
  .front-title {
    font-family: "Oswald", "Arial Narrow", sans-serif;
    font-weight: 600;
    color: var(--white);
    font-size: 92px;
    line-height: 1.08;
    text-align: center;
    letter-spacing: 1px;
  }
  .front-brand {
    position: absolute;
    left: 92px; top: 460px;
    width: 270px; height: 180px;
    background: var(--white);
    display: flex;
    flex-direction: column;
    align-items: center;
    justify-content: center;
    gap: 12px;
  }
  .brand-dot {
    width: 62px; height: 62px;
    border-radius: 50%;
    background: var(--royal);
  }
  .brand-name {
    font-weight: 700;
    font-size: 17px;
    color: var(--royal);
    text-transform: uppercase;
    text-align: center;
    line-height: 1.2;
    letter-spacing: 0.5px;
  }

  /* Back */
  .back-band {
    position: absolute;
    left: 0; top: 0;
    width: 100%; height: 370px;
    background: var(--sky);
  }
  .flyer--back .rule { height: 370px; background: var(--white); }
  .flyer--back .rule--left { left: 72px; }
  .flyer--back .rule--right { left: 376px; }
  .invite-card {
    position: absolute;
    left: 90px; top: 0;
    width: 274px; height: 500px;
    background: linear-gradient(170deg, var(--white) 30%, var(--sky-pale) 60%, var(--white) 85%);
    text-align: center;
    padding: 38px 14px 0;
  }
  .flourish {
    display: block;
    width: 66px; height: 8px;
    margin: 0 auto;
    border-radius: 4px;
    background: var(--royal);
    opacity: 0.55;
  }
  .invite-lead {
    margin-top: 22px;
    font-size: 18px;
    line-height: 1.3;
    color: var(--ink);
  }
  .special-guest {
    display: inline-block;
    margin-top: 16px;
    padding: 7px 16px;
    background: var(--royal);
    border-radius: 9px;
    color: var(--white);
    font-size: 21px;
    letter-spacing: 0.3px;
  }
  .invite-when {
    margin-top: 18px;
    font-size: 17px;
    color: var(--royal);
  }
  .flourish--lower { margin-top: 24px; }
  .find-us {
    margin-top: 22px;
    font-size: 19px;
    color: var(--ink);
  }
  .address {
    margin-top: 10px;
    font-size: 13.5px;
    line-height: 1.4;
    color: var(--royal);
  }
  .contact {
    position: absolute;
    left: 0; top: 528px;
    width: 100%;
    text-align: center;
    font-size: 18px;
    line-height: 1.42;
    color: var(--white);
    padding: 0 28px;
  }
  .contact-lead { color: var(--sky); display: block; }
</style>
</head>
<body>

  <section class="flyer flyer--front" aria-label="Flyer front">
    <span class="rule rule--left"></span>
    <span class="rule rule--right"></span>
    <div class="front-panel">
      <h1 class="front-title">BE<br>OUR<br>GUEST</h1>
    </div>
    <div class="front-brand">
      <span class="brand-dot"></span>
      <p class="brand-name">Harvest Gateway<br>Ministries</p>
    </div>
  </section>

  <section class="flyer flyer--back" aria-label="Flyer back">
    <div class="back-band"></div>
    <span class="rule rule--left"></span>
    <span class="rule rule--right"></span>
    <div class="invite-card">
      <span class="flourish" role="img" aria-label="Decorative flourish"></span>
      <p class="invite-lead">We would love to have<br>you join us as our</p>
      <p class="special-guest">SPECIAL GUEST</p>
      <p class="invite-when">this Sunday at 10am.</p>
      <span class="flourish flourish--lower" role="img" aria-label="Decorative flourish"></span>
      <p class="find-us">You can find us at</p>
      <p class="address">Harvest Gateway Family Church, 17-19 Meadowbrook Lane (Behind Farley), Pellham Brook Village, KL7 2RT</p>
    </div>
    <p class="contact">
      <span class="contact-lead">For more information or for a chat,</span>
      please call us on 07614 290457 / 07781 504316 or email church@hgfcuk.org
    </p>
  </section>

</body>
</html>
```